Hi, I need a clean, simple card to hand out to parents for my tutoring business (elementary). I would like the front of the card to have the moose logo below, reading a book. Back should be clean, centered text, no logo just information.

Target Market(s)

Elementary school parents

Industry/Entity Type

Tutoring

Contact Information for Business Card

Front of card:

Moose logo on left + text on right says "Bright Otter Tutoring"

Back of card:

MAYA PRESCOTT
email envelope icon + BrightOtterTutoring@quillpost.example

Licensed Harwell District Schools Teacher
Calderbrook University, M.S. Education

Font styles to use
Serif
Other font styles liked:
• Handwritten font for "Bright Otter Tutoring" and "Maya Prescott", all else should be serif font

Colors
fee18b
fdf9ce

Requirements
Must have
• Playful, clean, simple. Font listed below.

```html
<!DOCTYPE html>
<html lang="en">
<head>
<meta charset="utf-8">
<title>Bright Otter Tutoring – Business Card</title>
<link rel="stylesheet" href="https://fonts.googleapis.com/css2?family=Arvo:wght@400;700&family=Noto+Serif:wght@400&display=swap">
<style>
  :root {
    --backdrop: #e8e9e9;
    --card-light: #fdf9ce;
    --card-warm: #fee18b;
    --brand-red: #7a1a14;
    --name-green: #2f5a2c;
    --body-ink: #3a3a2a;
    --mark-brown: #9a5a2e;
    --card-shadow: rgba(60, 50, 10, 0.18);
  }
  * { box-sizing: border-box; margin: 0; padding: 0; }
  html, body {
    width: 1200px;
    height: 707px;
    overflow: hidden;
    background: var(--backdrop);
  }
  .sheet {
    width: 1200px;
    height: 707px;
    display: flex;
    align-items: center;
    justify-content: center;
    gap: 44px;
  }
  .card {
    width: 530px;
    height: 303px;
    border-radius: 3px;
    background: radial-gradient(ellipse at 50% 45%, var(--card-light) 0%, #fdf1b0 55%, var(--card-warm) 100%);
    box-shadow: 0 6px 18px var(--card-shadow);
    position: relative;
  }
  /* Front */
  .card-front {
    display: flex;
    align-items: center;
    justify-content: center;
    gap: 30px;
  }
  .brand-mark {
    width: 150px;
    height: 150px;
    border-radius: 50%;
    background: var(--mark-brown);
    flex: none;
  }
  .brand-name {
    font-family: "Arvo", serif;
    font-weight: 700;
    font-size: 40px;
    line-height: 1.0;
    color: var(--brand-red);
  }
  .brand-name span { display: block; }
  /* Back */
  .card-back {
    display: flex;
    flex-direction: column;
    align-items: center;
    justify-content: center;
    text-align: center;
  }
  .tutor-name {
    font-family: "Arvo", serif;
    font-weight: 700;
    font-size: 27px;
    letter-spacing: 0.5px;
    color: var(--name-green);
  }
  .tutor-email {
    display: flex;
    align-items: center;
    gap: 7px;
    margin-top: 6px;
    font-family: "Noto Serif", serif;
    font-size: 13px;
    color: var(--name-green);
  }
  .tutor-email svg { width: 15px; height: 11px; flex: none; }
  .credentials {
    margin-top: 16px;
    font-family: "Noto Serif", serif;
    font-size: 13px;
    line-height: 1.6;
    color: var(--body-ink);
  }
</style>
</head>
<body>
  <main class="sheet">
    <section class="card card-front" aria-label="Card front">
      <div class="brand-mark" aria-hidden="true"></div>
      <h1 class="brand-name"><span>Bright</span><span>Otter</span><span>Tutoring</span></h1>
    </section>

    <section class="card card-back" aria-label="Card back">
      <h2 class="tutor-name">MAYA PRESCOTT</h2>
      <p class="tutor-email">
        <svg viewBox="0 0 15 11" aria-hidden="true">
          <rect x="0" y="0" width="15" height="11" rx="1" fill="#2f5a2c"/>
          <path d="M1 1.2 L7.5 6.2 L14 1.2" fill="none" stroke="#fdf9ce" stroke-width="1.2"/>
        </svg>
        BrightOtterTutoring@quillpost.example
      </p>
      <p class="credentials">
        Licensed Harwell District Schools Teacher<br>
        Calderbrook University, M.S. Education
      </p>
    </section>
  </main>
</body>
</html>
```